Flyer-Design für Fahrschule gesucht
Zielgruppe
Wir sind eine Fahrschule/ Führerscheinausbildung/ Bildungsträger und benötigen für die verschiedenen Führerscheinklassen einen Informationsflyer.
Aufgabenstellung
Format DIN Lang zum Aufklappen
Der Flyer sollte so gestaltet sein das sich das sich die auf der Front durch Austausch eines Icon/ Logos oder Text die jeweilige Führerscheinklasse bzw Information recht einfach austauschen lässt. Rückseite auch immer gleich. Innendesign auch immer gleich bis auf die Texte die dann jeweils ausgetauscht werden müssen.
Würde ungern Fotos einsetzen da bei Fahrzeug oder personal Wechsel dieses immer wieder zu Problemen führt - ich würde lieber auf Icons setzen da diese dauerhaft bestand haben.

```html
<!DOCTYPE html>
<html lang="de">
<head>
<meta charset="utf-8">
<title>Fahrschule Flyer – Klasse B</title>
<link href="https://fonts.googleapis.com/css2?family=Open+Sans:wght@400;600;700;800&family=Black+Ops+One&display=swap" rel="stylesheet">
<style>
  :root {
    --yellow: #ffdc00;
    --dark: #1e1e1e;
    --white: #ffffff;
    --fold: #d2232a;
  }
  * { box-sizing: border-box; margin: 0; padding: 0; }
  html, body { width: 1200px; height: 1200px; overflow: hidden; background: var(--yellow); }
  .flyer {
    position: relative; width: 1200px; height: 1200px; overflow: hidden;
    background: var(--yellow);
    font-family: "Open Sans", Arial, sans-serif;
  }
  .panels { position: absolute; inset: 0; }
  .panels path { fill: var(--dark); stroke: var(--dark); stroke-width: 20; stroke-linejoin: round; }

  .block {
    position: absolute; text-align: center; line-height: 1.22;
    transform: translate(-50%, -50%) rotate(-12deg);
  }
  .on-dark { color: var(--white); }
  .on-yellow { color: var(--dark); }
  .accent { color: var(--yellow); }
  h2 { font-weight: 800; }

  .class-badge {
    position: absolute; left: 124px; top: 104px; width: 136px; height: 136px;
    background: var(--dark); border-radius: 20px; transform: rotate(45deg);
  }
  .class-letter {
    position: absolute; left: 192px; top: 176px; transform: translate(-50%, -50%);
    font-weight: 800; font-size: 84px; line-height: 1; color: var(--yellow);
  }
  .class-label {
    position: absolute; left: 124px; top: 112px; transform: translate(-50%, -50%) rotate(-45deg);
    font-weight: 800; font-size: 28px; letter-spacing: 1px; color: var(--dark);
  }

  .brand {
    position: absolute; left: 605px; top: 106px; transform: translate(-50%, -50%);
    display: flex; align-items: center; gap: 12px; white-space: nowrap;
    font-weight: 800; font-size: 40px; color: var(--white);
  }
  .brand-mark { width: 20px; height: 20px; border-radius: 50%; background: var(--yellow); }

  .headline {
    position: absolute; left: 971px; top: 87px; width: 380px; transform: translate(-50%, -50%);
    text-align: center; font-weight: 700; font-size: 29px; line-height: 1.35; color: var(--dark);
  }

  .holiday {
    left: 1040px; top: 268px; width: 300px; transform: translate(-50%, -50%) rotate(-8deg);
    font-size: 20px; font-weight: 600; line-height: 1.7;
  }
  .holiday .big { font-size: 27px; font-weight: 800; }

  .intensive { left: 300px; top: 452px; width: 360px; font-size: 18px; }
  .intensive h2 { font-size: 25px; margin-bottom: 8px; }
  .intensive .lead { font-weight: 700; font-size: 19px; margin-bottom: 16px; }
  .intensive .req { font-weight: 800; font-size: 19px; }

  .stamp {
    position: absolute; left: 711px; top: 336px;
    transform: translate(-50%, -50%) rotate(-12deg);
    border: 7px solid var(--dark); border-radius: 4px; padding: 6px 14px 4px;
    font-family: "Black Ops One", Impact, sans-serif; color: var(--dark);
    text-align: center; white-space: nowrap; line-height: 1.05;
  }
  .stamp .top { font-size: 27px; }
  .stamp .bottom { font-size: 58px; }

  .age {
    left: 1103px; top: 505px; width: 130px; transform: translate(-50%, -50%) rotate(-8deg);
    font-weight: 800; font-size: 25px; line-height: 1.25;
  }
  .age .num { display: block; font-size: 42px; }

  .theory { left: 835px; top: 640px; width: 340px; font-size: 17px; }
  .theory h2 { font-size: 26px; margin-bottom: 4px; }
  .theory .cta { margin-top: 18px; font-weight: 800; font-size: 17px; }

  .single { left: 445px; top: 766px; width: 320px; font-size: 16.5px; line-height: 1.2; }
  .single h2 { font-size: 26px; margin-bottom: 4px; }
  .single p + p { margin-top: 18px; }

  .car-icon {
    position: absolute; left: 174px; top: 1016px; width: 180px; height: 90px;
    transform: translate(-50%, -50%) rotate(-24deg);
    background: var(--yellow); border-radius: 40px 60px 18px 18px;
  }

  .group { left: 556px; top: 1052px; width: 300px; font-size: 17px; }
  .group h2 { font-size: 24px; margin-bottom: 4px; }
  .group .lead { font-weight: 700; font-size: 19px; margin-bottom: 16px; }

  .learn { left: 915px; top: 935px; width: 400px; font-size: 16px; line-height: 1.28; }
  .learn .claim { margin-top: 16px; font-weight: 800; font-size: 19px; }

  .fold-line { position: absolute; left: 600px; top: 0; width: 1px; height: 1200px; background: var(--fold); }
</style>
</head>
<body>
<main class="flyer">
  <svg class="panels" width="1200" height="1200" viewBox="0 0 1200 1200" aria-hidden="true">
    <path d="M-20 -20 L300 -20 L-20 40 Z"/>
    <path d="M318 -20 L712 -20 L814 156 L430 212 Z"/>
    <path d="M1176 -20 L1220 -20 L1220 40 Z"/>
    <path d="M842 184 L1220 132 L1220 372 L986 420 Z"/>
    <path d="M-20 304 L10 326 L-20 344 Z"/>
    <path d="M30 338 L524 248 L566 532 L110 662 Z"/>
    <path d="M592 556 L984 446 L1088 674 L692 822 Z"/>
    <path d="M1124 702 L1220 680 L1220 962 L1176 972 Z"/>
    <path d="M-20 780 L204 694 L330 972 L412 1220 L-20 1220 Z"/>
    <path d="M354 994 L674 848 L774 1220 L436 1220 Z"/>
  </svg>

  <div class="class-badge"></div>
  <span class="class-letter">B</span>
  <span class="class-label">KLASSE</span>

  <div class="brand"><span class="brand-mark"></span>Spurwerk</div>
  <p class="headline">In kürzester Zeit zum Führerschein!</p>

  <div class="block holiday on-dark">
    Mache Deinen Führerschein<br>auch in den<br><span class="big accent">Ferien</span><br>oder<br>im <span class="big accent">Urlaub</span>!
  </div>

  <div class="block intensive on-dark">
    <h2 class="accent">INTENSIVKURSE</h2>
    <p class="lead">Hast Du wenig Zeit und möchtest Du den Führerschein in Recordzeit machen?</p>
    <p class="req">Voraussetzung:</p>
    <p>Der Führerscheinantrag muss vor Beginn (ca. 6 Wochen) des Intensiv­kurses gestellt werden damit der Prüfauftrag rechtzeitig erteilt wird.</p>
  </div>

  <div class="stamp">
    <div class="top">FÜHRERSCHEIN IN</div>
    <div class="bottom">10 TAGEN</div>
  </div>

  <div class="block age on-yellow">Auch ab<span class="num">17</span>Jahre!</div>

  <div class="block theory on-dark">
    <h2>THEORIE</h2>
    <p>Können denn Theoriestunden wirklich Spaß machen? Klar – bei uns gibt’s keinen der den Stoff einfach nur trocken runterleiert. Lass Dich positiv überraschen!</p>
    <p class="cta">TESTE UNS JETZT UND SICHER DIR DEINE KOSTENLOSE<br><span class="accent">THEORIE-SCHNUPPERSTUNDE!</span></p>
  </div>

  <div class="block single on-yellow">
    <h2>Einzelkurse</h2>
    <p>Ganz nach persönlicher Situation können wir mit Dir Deinen Intensiv­kurs planen, der innerhalb unserer Kapazitäten abgestimmt wird.</p>
    <p>Wir helfen Dir gerne bei der persön­lichen Planung Deines Intensivkur­ses. Bitte mache direkt einen Termin bei uns. Wir freuen uns auf deinen Anruf!</p>
  </div>

  <div class="car-icon" role="img" aria-label="Auto-Icon in Gelb"></div>

  <div class="block group on-dark">
    <h2 class="accent">Gruppenkurse</h2>
    <p class="lead">Bisher haben wir eine Beste­herquote von annähernd 100%.</p>
    <p>WICHTIG!<br>Wir können die Intensivkurse nur jeweils nach unsereren Kapazitäten anbieten.</p>
  </div>

  <div class="block learn on-yellow">
    <p>Den Stoff kann man viel besser an interessanten Beispielen lernen und sich einprägen. Willst Du wissen was für die Prüfung wichtig ist? Bei uns gibt’s viele praktische Tipps. Wir gehen mit Dir alle relevanten Themen durch und üben an echten Prüfungsszenen. Wenn es einem Schüler etwas schwer fällt in der Gruppe mitzuhalten, dann geben wir auch gerne Nachhilfe. In unseren fünf Filialen hast Du fast immer die Möglichkeit an unterschiedlichen Wochentagen den Stoff zu lernen den Du brauchst – auch wenn Du mal einen Termin verpasst hast.</p>
    <p class="claim">Bei uns kann jeder die Prüfung packen!</p>
  </div>

  <div class="fold-line"></div>
</main>
</body>
</html>
```